Forward Thinking Civil Engineering Company Brochure

Objective: Create a visually compelling marketing folder that effectively communicates the company’s commitment to technical excellence, quality control, responsiveness, and sustainability. Design cascading card inserts for more details on each service area.

Use: The folder will be used for client meetings, proposals, and trade shows to present services, capabilities, and case studies in a structured and engaging manner. Front, back, and pockets may be used for design but one pocket should have location for business card.

Company Identity: Modern, innovative, and sustainability-focused.
Color Scheme/Typography: Align with our brand (see attached... the neutral color can be adjusted)
Style: Clean, professional, and forward-thinking perhaps with subtle technical elements (blueprints, grids, engineering icons).

Folder Size: Standard 9” x 12” presentation folder with pockets.
Branding Elements: Must include certifications (see www.q7veng.com homepage for the certifications...HUB, SBA etc)
Logo placement (front cover and inside pocket).

q7veng.com is old website do not pull branding concepts

Cascading Design: Insert cards should be stacked inside the folder, with visible section titles when inserted.
Left Pocket – 4 Cascading Cards (About Q7V, PS&E, Geotechnical Engineering, Construction Material Testing)
Largest: 8.75" x 11.5"
Medium-Large: 8.75" x 10.75"
Medium: 8.75" x 10"
Smallest: 8.75" x 9.25"
Right Pocket – 4 Cascading Cards (Construction, Engineering & Testing, Construction Management, Environmental Engineering, Drone and GIS Services)
Largest: 8.75" x 11.5"
Medium: 8.75" x 10"
Smallest: 8.75" x 9.25"

```html
<!DOCTYPE html>
<html lang="en">
<head>
<meta charset="utf-8">
<title>Q7V Engineering – Presentation Folder</title>
<link rel="stylesheet" href="https://fonts.googleapis.com/css2?family=Montserrat:wght@400;600;700;800&family=Open+Sans:wght@400;600&display=swap">
<style>
:root{
  --navy:#2e3b4c;
  --navy-deep:#253141;
  --navy-pocket:#34445a;
  --orange:#c6612a;
  --orange-light:#d9783f;
  --white:#ffffff;
  --stage:#dcdcdc;
  --photo-sky:#8fb2cf;
  --photo-ground:#9a7e63;
  --photo-steel:#8c949c;
  --badge-mark:#c9ced6;
}
*{box-sizing:border-box;margin:0;padding:0}
html,body{width:1200px;height:2192px;overflow:hidden;background:var(--stage)}
body{position:relative;font-family:"Open Sans",Arial,sans-serif;color:var(--white)}
.spread{position:absolute;left:80px;width:1040px;height:693px;display:flex;box-shadow:0 6px 18px rgba(0,0,0,.25)}
.spread--outer{top:28px}
.spread--inside{top:749px}
.spread--cards{top:1470px;gap:0}
.panel{position:relative;width:520px;height:693px;overflow:hidden}
.panel--navy{background:var(--navy)}
.panel--orange{background:var(--orange);padding:22px 24px}

/* logo wordmark */
.wordmark{display:flex;align-items:center;gap:10px;font-family:"Montserrat",sans-serif;font-weight:700;letter-spacing:.08em;color:var(--white)}
.wordmark__square{width:22px;height:22px;background:var(--orange)}

/* back cover */
.beams{position:absolute;inset:0}
.back-logo{position:absolute;left:0;right:0;top:330px;display:flex;flex-direction:column;align-items:center;gap:14px}
.back-logo .wordmark{font-size:26px}
.contact{font-size:12px;line-height:1.7;text-align:center;color:#dfe5ec}
.contact__row{display:flex;align-items:center;justify-content:center;gap:6px}

/* front cover */
.front-logo{position:absolute;left:28px;top:24px;font-size:14px}
.headline{position:absolute;left:28px;top:62px;font-family:"Montserrat",sans-serif;font-weight:800;font-size:50px;line-height:1;color:var(--orange);text-transform:uppercase;z-index:2;letter-spacing:.01em}
.headline span{display:block}
.cover-photo{position:absolute;left:0;right:0;top:50px;height:460px;background:linear-gradient(180deg,var(--photo-sky) 0%,#b9cde0 55%,var(--photo-ground) 80%,#6f5a47 100%)}
.cover-photo::after{content:"";position:absolute;inset:0;background:linear-gradient(180deg,rgba(46,59,76,.55) 0%,rgba(46,59,76,0) 40%)}
.badges{position:absolute;left:28px;right:28px;bottom:26px;display:grid;grid-template-columns:repeat(4,1fr);gap:10px}
.badge{height:60px;background:var(--white);display:flex;align-items:center;justify-content:center}
.badge__mark{width:46px;height:30px;background:var(--badge-mark);border-radius:3px}

/* section bars */
.bar{height:30px;background:var(--navy);display:flex;align-items:center;padding:0 12px;font-family:"Montserrat",sans-serif;font-weight:700;font-size:12px;letter-spacing:.06em;text-transform:uppercase;position:relative;overflow:hidden}
.bar::after{content:"";position:absolute;right:-10px;top:0;width:120px;height:30px;background:linear-gradient(100deg,transparent 30%,rgba(255,255,255,.5) 31%,rgba(255,255,255,.5) 36%,transparent 37%,transparent 50%,rgba(255,255,255,.8) 51%,rgba(255,255,255,.8) 60%,transparent 61%)}
.photo{background:linear-gradient(180deg,var(--photo-sky) 0%,#c2d2df 45%,var(--photo-steel) 70%,var(--photo-ground) 100%)}
.photo--site{background:linear-gradient(180deg,#b9c7d3 0%,var(--photo-steel) 50%,#7b6a58 100%)}
.photo--building{background:linear-gradient(180deg,#9fbdd6 0%,#c7a37f 55%,#8a5b3d 100%)}
.row{display:flex;gap:16px;margin-top:12px}
.copy{flex:1;font-size:11px;line-height:1.6}

.features{display:flex;gap:14px;margin-top:16px}
.feature{flex:1;height:150px;background:var(--white);color:var(--navy);padding:14px 10px;text-align:center;display:flex;flex-direction:column;align-items:center;gap:8px}
.feature__title{font-family:"Montserrat",sans-serif;font-weight:700;font-size:11px;color:var(--orange)}
.feature__text{font-size:10px;line-height:1.5}
.feature svg{width:34px;height:34px}

/* inside folder */
.card{position:absolute;left:22px;right:22px;top:28px;bottom:0;background:var(--orange);padding:16px 18px}
.card--tier{top:14px;left:30px;right:30px;background:var(--orange-light)}
.pocket{position:absolute;left:0;right:0;bottom:0;height:270px;background:var(--navy-pocket);box-shadow:0 -4px 10px rgba(0,0,0,.3)}
.pocket svg.pocket-edge{position:absolute;top:-28px;left:0;width:520px;height:30px}
.pocket .badges{bottom:auto;top:40px}
.card-slot{position:absolute;left:50%;transform:translateX(-50%);bottom:40px;width:230px;height:100px;border:1px solid rgba(255,255,255,.35)}
.card-slot::before,.card-slot::after{content:"";position:absolute;top:-2px;width:30px;height:3px;background:var(--navy-deep)}
.card-slot::before{left:-2px}.card-slot::after{right:-2px}
.pocket .wordmark{position:absolute;left:50%;transform:translateX(-50%);top:72px;font-size:18px}
</style>
</head>
<body>

<!-- outer folder: back + front cover -->
<section class="spread spread--outer">
  <div class="panel panel--navy back-cover">
    <svg class="beams" viewBox="0 0 520 693" preserveAspectRatio="none" aria-hidden="true">
      <polygon points="0,70 260,0 330,0 0,190" fill="#ffffff" opacity=".9"/>
      <polygon points="0,210 360,0 380,0 0,240" fill="#ffffff" opacity=".45"/>
      <polygon points="0,255 400,0 410,0 0,268" fill="#ffffff" opacity=".25"/>
    </svg>
    <div class="back-logo">
      <div class="wordmark"><span class="wordmark__square"></span>Q7V ENGINEERING</div>
      <div class="contact">
        <div class="contact__row">
          <svg width="11" height="11" viewBox="0 0 24 24" aria-hidden="true"><path fill="#fff" d="M6.6 10.8a15 15 0 0 0 6.6 6.6l2.2-2.2a1 1 0 0 1 1-.25 11.4 11.4 0 0 0 3.6.57 1 1 0 0 1 1 1V20a1 1 0 0 1-1 1A17 17 0 0 1 3 4a1 1 0 0 1 1-1h3.5a1 1 0 0 1 1 1c0 1.25.2 2.45.57 3.6a1 1 0 0 1-.25 1z"/></svg>
          (555) 014-2290
        </div>
        <div>www.q7veng.com</div>
      </div>
    </div>
  </div>

  <div class="panel panel--navy front-cover">
    <div class="cover-photo" role="img" aria-label="Engineer holding a blueprint in front of a building under construction"></div>
    <div class="wordmark front-logo"><span class="wordmark__square"></span>Q7V ENGINEERING</div>
    <h1 class="headline"><span>15 Years of</span><span>Experience</span></h1>
    <div class="badges" aria-label="Certifications">
      <div class="badge"><span class="badge__mark"></span></div>
      <div class="badge"><span class="badge__mark"></span></div>
      <div class="badge"><span class="badge__mark"></span></div>
      <div class="badge"><span class="badge__mark"></span></div>
      <div class="badge"><span class="badge__mark"></span></div>
      <div class="badge"><span class="badge__mark"></span></div>
      <div class="badge"><span class="badge__mark"></span></div>
      <div class="badge"><span class="badge__mark"></span></div>
    </div>
  </div>
</section>

<!-- inside folder with pockets and cascading cards -->
<section class="spread spread--inside">
  <div class="panel panel--navy inside-left">
    <div class="card card--tier"></div>
    <div class="card">
      <div class="bar">About Us</div>
      <div class="photo photo--building" style="height:130px;margin-top:12px" role="img" aria-label="Company office building exterior"></div>
      <div class="features">
        <div class="feature" style="height:100px"><svg viewBox="0 0 40 40" aria-hidden="true"><circle cx="20" cy="20" r="17" fill="none" stroke="#c6612a" stroke-width="3"/><path d="M12 20l6 6 11-12" fill="none" stroke="#c6612a" stroke-width="3"/></svg></div>
        <div class="feature" style="height:100px"><svg viewBox="0 0 40 40" aria-hidden="true"><circle cx="20" cy="20" r="17" fill="none" stroke="#c6612a" stroke-width="3"/><path d="M12 20l6 6 11-12" fill="none" stroke="#c6612a" stroke-width="3"/></svg></div>
        <div class="feature" style="height:100px"><svg viewBox="0 0 40 40" aria-hidden="true"><circle cx="20" cy="20" r="17" fill="none" stroke="#c6612a" stroke-width="3"/><path d="M12 20l6 6 11-12" fill="none" stroke="#c6612a" stroke-width="3"/></svg></div>
      </div>
    </div>
    <div class="pocket">
      <svg class="pocket-edge" viewBox="0 0 520 30" preserveAspectRatio="none" aria-hidden="true"><polygon points="0,30 0,8 520,28 520,30" fill="#34445a"/></svg>
      <div class="badges" aria-label="Certifications">
        <div class="badge"><span class="badge__mark"></span></div>
        <div class="badge"><span class="badge__mark"></span></div>
        <div class="badge"><span class="badge__mark"></span></div>
        <div class="badge"><span class="badge__mark"></span></div>
        <div class="badge"><span class="badge__mark"></span></div>
        <div class="badge"><span class="badge__mark"></span></div>
        <div class="badge"><span class="badge__mark"></span></div>
        <div class="badge"><span class="badge__mark"></span></div>
      </div>
    </div>
  </div>

  <div class="panel panel--navy inside-right">
    <div class="card card--tier"></div>
    <div class="card">
      <div class="bar">Construction Management</div>
      <div class="photo photo--site" style="height:110px;margin-top:12px" role="img" aria-label="Crew working on a rooftop"></div>
      <div class="bar" style="margin-top:14px">Construction, Engineering &amp; Inspection</div>
      <div class="photo" style="height:110px;margin-top:12px" role="img" aria-label="Inspector on a large roof deck"></div>
    </div>
    <div class="pocket">
      <svg class="pocket-edge" viewBox="0 0 520 30" preserveAspectRatio="none" aria-hidden="true"><polygon points="0,30 0,28 520,8 520,30" fill="#34445a"/></svg>
      <div class="card-slot" aria-label="Business card slot"></div>
    </div>
  </div>
</section>

<!-- insert cards, flat -->
<section class="spread spread--cards">
  <article class="panel panel--orange card-about">
    <div class="bar">About Us</div>
    <div class="row">
      <p class="copy">Q7V Engineering delivers civil, geotechnical and testing services across the region with a focus on quality, speed and lasting value.</p>
      <div class="photo photo--building" style="width:230px;height:140px" role="img" aria-label="Company office building exterior"></div>
    </div>
    <div class="features">
      <div class="feature">
        <svg viewBox="0 0 40 40" aria-hidden="true"><circle cx="20" cy="20" r="17" fill="none" stroke="#c6612a" stroke-width="3"/><path d="M20 10v10l7 5" fill="none" stroke="#c6612a" stroke-width="3"/></svg>
        <div class="feature__title">15+ Years Experience</div>
        <div class="feature__text">Over 15 years of trusted field experience</div>
      </div>
      <div class="feature">
        <svg viewBox="0 0 40 40" aria-hidden="true"><circle cx="20" cy="20" r="17" fill="none" stroke="#c6612a" stroke-width="3"/><path d="M12 20l6 6 11-12" fill="none" stroke="#c6612a" stroke-width="3"/></svg>
        <div class="feature__title">Full Service</div>
        <div class="feature__text">Full range of testing and design services</div>
      </div>
      <div class="feature">
        <svg viewBox="0 0 40 40" aria-hidden="true"><rect x="5" y="5" width="30" height="30" fill="none" stroke="#c6612a" stroke-width="3"/><path d="M12 20l6 6 11-12" fill="none" stroke="#c6612a" stroke-width="3"/></svg>
        <div class="feature__title">Certified Team</div>
        <div class="feature__text">Certified and licensed staff on every job</div>
      </div>
    </div>
    <div class="bar" style="margin-top:18px">Geotechnical Engineering &amp; Material Testing</div>
    <div class="row">
      <p class="copy">Soil borings, lab testing and foundation reports that guide safe, cost-effective design from site study to final build.</p>
      <div class="photo photo--site" style="width:230px;height:120px" role="img" aria-label="Technicians testing soil on a job site"></div>
    </div>
    <div class="photo" style="height:66px;margin-top:14px" role="img" aria-label="Wide view of an active construction site"></div>
  </article>

  <article class="panel panel--orange card-services">
    <div class="bar">Construction Management</div>
    <div class="row">
      <p class="copy">We manage schedule, budget and quality so every project moves from plan to completion with clear reporting.</p>
      <div class="photo photo--site" style="width:230px;height:110px" role="img" aria-label="Crew working on a rooftop"></div>
    </div>
    <div class="bar" style="margin-top:16px">Construction, Engineering &amp; Inspection</div>
    <div class="row">
      <p class="copy">Field inspection and material testing keep work aligned with plans, specs and local code requirements.</p>
      <div class="photo" style="width:230px;height:110px" role="img" aria-label="Inspector on a large roof deck"></div>
    </div>
    <div class="bar" style="margin-top:16px">Drone Services</div>
    <div class="row">
      <p class="copy">Aerial surveys capture site progress and accurate mapping data.</p>
      <div class="photo photo--site" style="width:230px;height:70px" role="img" aria-label="Aerial view of a site under construction"></div>
    </div>
    <div class="bar" style="margin-top:16px">GIS Services</div>
    <div class="row">
      <p class="copy">Spatial data and mapping tools support planning and asset records.</p>
      <div class="photo" style="width:230px;height:88px" role="img" aria-label="Crane lifting steel at a building site"></div>
    </div>
  </article>
</section>

</body>
</html>
```